Velmora Commercial Finance Information Brochure

This brochure will be sent out to clients via A4 PDF on an email to showcase what our company has to offer. We are a commercial finance brokerage, that specialises in property finance. We would like to see designs following our colour scheme. The final design should demonstrate our professionalism and reliability.
I have attached our logo and also a few bullet points on our information and what we can offer. These can be slightly reworded for conciseness. Or leave the text sections as filler and I can fill these in.
I have also attached an overview of our colour scheme and design styling for your consideration.
Target Market(s)
Property Developers
Industry/Entity Type
Financial Services
Look and feel
Each slider illustrates characteristics of the customer's brand and the style your logo design should communicate.

```html
<!DOCTYPE html>
<html lang="en">
<head>
<meta charset="utf-8">
<title>Velmora Finance – Information Brochure</title>
<link rel="stylesheet" href="https://fonts.googleapis.com/css2?family=Montserrat:wght@700&family=Questrial&display=swap">
<style>
  :root {
    --backdrop: #444a58;
    --paper: #f3f6f7;
    --paper-white: #ffffff;
    --brand-blue: #1b3c9c;
    --brand-blue-deep: #12286e;
    --brand-green: #248a3e;
    --brand-green-deep: #1a6630;
    --ink: #1c2340;
    --ink-soft: #2a3150;
    --rule: #d6dbe2;
  }
  * { margin: 0; padding: 0; box-sizing: border-box; }
  html, body { width: 1200px; height: 779px; overflow: hidden; }
  body {
    background: var(--backdrop);
    font-family: "Questrial", Arial, sans-serif;
    color: var(--ink);
    position: relative;
  }
  .page {
    position: absolute;
    top: 42px;
    width: 497px;
    height: 703px;
    overflow: hidden;
  }
  .page--cover { left: 83px; background: var(--paper); }
  .page--info { left: 623px; background: var(--paper-white); }
  .page-art { position: absolute; inset: 0; width: 100%; height: 100%; }

  .cover-name {
    position: absolute;
    left: 62px;
    top: 326px;
    width: 310px;
    text-align: center;
    color: var(--brand-blue);
    font-family: "Montserrat", Arial, sans-serif;
    font-weight: 700;
    line-height: 1;
  }
  .cover-name__main { display: block; font-size: 44px; letter-spacing: 0.5px; }
  .cover-name__sub { display: block; font-size: 18px; letter-spacing: 13px; margin-top: 8px; padding-left: 13px; }

  .header-name {
    position: absolute;
    left: 284px;
    top: 30px;
    width: 196px;
    text-align: center;
    color: var(--paper-white);
    font-family: "Montserrat", Arial, sans-serif;
    font-weight: 700;
    line-height: 1;
  }
  .header-name__main { display: block; font-size: 29px; letter-spacing: 0.3px; }
  .header-name__sub { display: block; font-size: 11px; letter-spacing: 7px; margin-top: 6px; padding-left: 7px; }

  .section { position: absolute; left: 19px; right: 19px; }
  .section__title {
    display: flex;
    align-items: center;
    gap: 10px;
    font-family: "Montserrat", Arial, sans-serif;
    font-size: 16.5px;
    font-weight: 700;
    color: var(--ink);
    letter-spacing: 0.2px;
    line-height: 1;
  }
  .section__title::after {
    content: "";
    flex: 1;
    height: 1px;
    background: var(--rule);
  }
  .section__body { position: relative; margin-top: 5px; }
  .section__body::before {
    content: "";
    position: absolute;
    top: 3px;
    left: 10px;
    border-left: 7px solid var(--brand-blue);
    border-top: 4.5px solid transparent;
    border-bottom: 4.5px solid transparent;
  }
  .section__body p {
    font-size: 9px;
    line-height: 12.6px;
    letter-spacing: 0.25px;
    text-align: justify;
    color: var(--ink-soft);
    margin-bottom: 12.4px;
  }
  .section--who { top: 203px; }
  .section--who .section__body { padding-left: 29px; }
  .section--mission { top: 277px; }
  .section--mission .section__body { padding-left: 24px; }
  .section--vision { top: 471px; }
  .section--vision .section__body { padding-left: 24px; margin-top: 7px; }
  .section--vision .section__body p { font-size: 9.8px; line-height: 13.8px; letter-spacing: 0.3px; }

  .contact {
    position: absolute;
    left: 375px;
    top: 627px;
    padding-left: 4px;
    border-left: 1px solid var(--ink);
    font-size: 5.6px;
    line-height: 8.3px;
    color: var(--ink);
    list-style: none;
  }
  .contact__address { margin-bottom: 2px; }
  .contact li { display: flex; align-items: center; gap: 3px; }
  .contact svg { width: 5px; height: 5px; fill: var(--brand-green-deep); }
</style>
</head>
<body>

<section class="page page--cover" aria-label="Brochure cover">
  <svg class="page-art" viewBox="0 0 621 879" preserveAspectRatio="none">
    <defs>
      <linearGradient id="cover-graphic" x1="0" y1="0" x2="1" y2="1">
        <stop offset="0" stop-color="var(--brand-blue)"/>
        <stop offset="1" stop-color="var(--brand-green)"/>
      </linearGradient>
      <linearGradient id="cover-column" x1="0" y1="0" x2="1" y2="0">
        <stop offset="0" stop-color="var(--brand-blue-deep)"/>
        <stop offset="1" stop-color="var(--brand-green-deep)"/>
      </linearGradient>
    </defs>
    <rect class="cover-frame" x="38" y="36" width="546" height="807" fill="none" stroke="var(--brand-blue)" stroke-width="3"/>
    <g role="img" aria-label="Decorative folded ribbon graphic in brand blue and green">
      <rect x="292" y="0" width="329" height="232" fill="url(#cover-graphic)"/>
      <rect x="507" y="232" width="114" height="647" fill="url(#cover-column)"/>
    </g>
  </svg>
  <h1 class="cover-name">
    <span class="cover-name__main">VELMORA</span>
    <span class="cover-name__sub">FINANCE</span>
  </h1>
</section>

<section class="page page--info" aria-label="Company information">
  <svg class="page-art" viewBox="0 0 621 879" preserveAspectRatio="none">
    <defs>
      <linearGradient id="header-graphic" x1="0" y1="0" x2="1" y2="1">
        <stop offset="0" stop-color="var(--brand-blue)"/>
        <stop offset="0.55" stop-color="var(--brand-green-deep)"/>
        <stop offset="1" stop-color="var(--brand-blue-deep)"/>
      </linearGradient>
    </defs>
    <rect x="0" y="0" width="621" height="220" fill="url(#header-graphic)" role="img" aria-label="Header graphic: folded ribbon over a financial market screen, in blue and green"/>
    <polygon points="0,801 311,801 273,838 0,838" fill="var(--brand-blue)"/>
    <line x1="216" y1="820" x2="457" y2="820" stroke="var(--brand-green)" stroke-width="1.5"/>
  </svg>

  <div class="header-name">
    <span class="header-name__main">VELMORA</span>
    <span class="header-name__sub">FINANCE</span>
  </div>

  <article class="section section--who">
    <h2 class="section__title">WHO WE ARE</h2>
    <div class="section__body">
      <p>As former lenders and developers ourselves, we intimately understand the inefficiencies that plague deals in the market today. We’ve experienced the frustration of tight time limits on deals and the exasperating feeling of brokers wasting precious time collecting information. It’s enough to drive developers and lenders insane!</p>
    </div>
  </article>

  <article class="section section--mission">
    <h2 class="section__title">MISSION</h2>
    <div class="section__body">
      <p>That’s why we founded Velmora Finance – to be the efficient and reliable link that connects developers and lenders. We’ve streamlined our processes to eliminate unnecessary hurdles, enabling clear and swift communication between all parties involved. No more wasted time. No more unnecessary stress.</p>
      <p>With our expertise and industry insights, we’ve developed a unique approach that simplifies the financing journey. From the initial consultation to the final funding, we’re here to guide you every step of the way. Our goal? To make commercial financing a smooth and enjoyable experience for you.</p>
      <p>With our background in the asset management industry, we have cultivated a black book of fund managers, institutions, UHNWI and private equity lenders that we can call on for non-traditional lending.</p>
    </div>
  </article>

  <article class="section section--vision">
    <h2 class="section__title">VISION</h2>
    <div class="section__body">
      <p>Velmora Finance was created to satisfy a need in the market that has been far too overlooked. Efficiency. Efficiency is at the heart of our operations, and we pride ourselves on our ability to secure the best financing options swiftly and effectively for our clients. By employing cutting-edge technology and streamlining our internal processes, we have cultivated a seamless and time-saving approach to finance brokering. Having been a developer, we understand the stresses and headaches associated with building, let alone all the paperwork and emails backwards and forwards between yourself and brokers to attain the necessary financing.</p>
    </div>
  </article>

  <ul class="contact">
    <li class="contact__address">214 Kestrel Row<br>Harbourton, Alaska 39120</li>
    <li><svg viewBox="0 0 10 10"><path d="M2 0h2l1 3-1.5 1a6 6 0 0 0 2.5 2.5L7 5l3 1v2a2 2 0 0 1-2 2A8 8 0 0 1 0 2a2 2 0 0 1 2-2z"/></svg>555-210-4418</li>
    <li><svg viewBox="0 0 10 10"><path d="M2.5 0h5a1 1 0 0 1 1 1v8a1 1 0 0 1-1 1h-5a1 1 0 0 1-1-1V1a1 1 0 0 1 1-1zm.5 1.5v6h4v-6z"/></svg>555-730-9162</li>
    <li><svg viewBox="0 0 10 10"><path d="M0 2h10v6H0zm1 1v.4l4 2.6 4-2.6V3z"/></svg>hello@velmorafinance.example</li>
    <li><svg viewBox="0 0 10 10"><circle cx="5" cy="5" r="4.5"/></svg>www.velmorafinance.example</li>
  </ul>
</section>

</body>
</html>
```